Thistle Cafe's Web Page
Thank you for all the hardwork. Happy to see there are so many beautiful artworks. We have tried very hard to select the final winner. All the best in the year of Rabbit!!
We will post more contest later.Just stay tune!!
Good luck for all!!
good luck tremiko !!!
kindly rate template
thank you.
Can you kindly Rate our templates.
so that we will able to guess our work judgment.. how much effort we need more to create exact design!!!
Hi Guys! The reason I justified the work of Quillaro work is the outline of the web page not the software itself. When I look at the designs and the tones are mostly in black color and I think you will do the same thing as me. Do you all agree??
Corvel! your artwork is quite interesting too! Especially the slogan you made!! Your design is one of our consideration too!!
well i am waiting for your feedback. thanks
this whole thing is turning to a joke. enjoy
@ SirPlonk, Are you serious? You are only seeing part of my design. Please do not judge. Your comment is very offensive and you are belittling my work.
you're not serious are you ?
I think the design made by Quillarowork is quite attractive.
pomlet42 > Please let us know which designs you like so far. regards
Please check the design and rate :)
Best wishes
Wow! Quillarowork's design is quite nice. What's in the photo? Looks good!!
I found a website is quite interesting - http://www.brasvelo.com.au/. The designs that I recieved are similar. I hope the black color is not the only choice for us. Keep it going! Guys.Overall, the layouts are OK.
Just to verify, you will have both a set menu and a daily specials menu, is that correct. What other pages where you looking for on your site?
We are still renovating. It will be a good idea to spare some space for our cafe and our menu and special. We will be listen to any good suggestion!!
Logo has been uploaded
Thanks a lot :) I'M IN :)
Hi PH, Can you upload your logo so we know where to start? Thanks
We have a logo designed. It may be helpful to get some ideas. Please ask for it or browse the past projects (around late December) if needed.

```html
<!DOCTYPE html>
<html lang="en">
<head>
<meta charset="utf-8">
<title>Thistle Cafe</title>
<link href="https://fonts.googleapis.com/css2?family=Didact+Gothic&family=Arimo:wght@400&display=swap" rel="stylesheet">
<style>
  :root {
    --bg: #1a0c0c;
    --panel: #140909;
    --orange: #e8561c;
    --orange-soft: #f07a3c;
    --cream: #f6e8dc;
    --white: #ffffff;
    --nav: #2a1716;
    --nav-edge: #3d2422;
  }
  * { margin: 0; padding: 0; box-sizing: border-box; }
  html, body { width: 1200px; height: 901px; overflow: hidden; background: var(--bg); }
  .page { position: relative; width: 1200px; height: 901px; background: radial-gradient(ellipse at 50% 30%, #241111 0%, var(--bg) 70%); font-family: "Arimo", Arial, sans-serif; color: var(--white); }

  .brand { position: absolute; top: 38px; left: 0; width: 1200px; display: flex; justify-content: center; align-items: center; gap: 18px; }
  .brand-dot { width: 30px; height: 30px; border-radius: 50%; background: var(--orange); }
  .brand-name { font-family: "Didact Gothic", sans-serif; font-size: 86px; line-height: 1; color: var(--cream); letter-spacing: 1px; }

  .panel { position: absolute; left: 80px; top: 172px; width: 1040px; height: 616px; border: 3px solid var(--orange); border-radius: 46px; background: linear-gradient(180deg, #1d0d0c 0%, var(--panel) 100%); box-shadow: 0 0 14px rgba(232,86,28,.35); overflow: hidden; }

  .nav { position: absolute; left: 125px; top: 0; width: 780px; height: 50px; background: linear-gradient(180deg, var(--nav-edge), var(--nav)); border-radius: 0 0 26px 26px; display: flex; justify-content: center; align-items: center; gap: 22px; font-family: "Didact Gothic", sans-serif; font-size: 27px; }
  .nav a { color: var(--white); text-decoration: none; }
  .nav .sep { width: 7px; height: 7px; border-radius: 50%; background: var(--orange); }

  .col { position: absolute; top: 100px; }
  .col-about { left: 76px; width: 380px; }
  .col-special { left: 583px; width: 400px; }
  .col h2 { font-family: "Didact Gothic", sans-serif; font-weight: 400; font-size: 40px; color: var(--orange-soft); margin-bottom: 18px; white-space: nowrap; }
  .col h2 .slash { color: var(--white); margin-right: 8px; }
  .about-text { font-size: 18.5px; line-height: 25.5px; }
  .dishes { list-style: none; font-size: 18.5px; margin-top: 34px; }
  .dishes li { height: 48.5px; }

  .gallery { position: absolute; left: 0; bottom: 0; width: 100%; height: 184px; display: flex; gap: 4px; }
  .photo { flex: 1; }
  .photo-noodles { background: radial-gradient(circle at 50% 50%, #d9a15a, #7a4a22 70%, #2a1a10); }
  .photo-bowl { background: radial-gradient(circle at 50% 55%, #c8532a, #6b7d3a 45%, #1e1a16 80%); }
  .photo-wok { background: radial-gradient(circle at 50% 55%, #b8482a, #4f6a2c 45%, #1a1412 80%); }
  .photo-duck { background: radial-gradient(circle at 45% 55%, #d87a3a, #e8ddd0 50%, #7a2a1a 90%); }

  .footer { position: absolute; top: 796px; left: 0; width: 1200px; text-align: center; font-size: 15px; color: var(--white); }
</style>
</head>
<body>
<div class="page">
  <header class="brand">
    <span class="brand-dot"></span>
    <span class="brand-name">Thistle</span>
  </header>

  <main class="panel">
    <nav class="nav">
      <a href="#">Home</a><span class="sep"></span>
      <a href="#">About Us</a><span class="sep"></span>
      <a href="#">Menus</a><span class="sep"></span>
      <a href="#">Booking Enquiry</a><span class="sep"></span>
      <a href="#">Contact</a>
    </nav>

    <section class="col col-about">
      <h2><span class="slash">/</span>About Thistle Cafe</h2>
      <p class="about-text">Our cafe is not focused on a large A-la Carte menu. We serve our food according to the weather, the freshest ingredients and the likeness of our customers. We put eastern ideas into western cuisine. For example, we used crsipy boneless Peking Duck with seasoned fruit to make our wraps or using grilled teriyaki beef to serve our open sandwiches.</p>
    </section>

    <section class="col col-special">
      <h2><span class="slash">/</span>Daily Special Menu</h2>
      <ul class="dishes">
        <li>Dish One - some information on it.</li>
        <li>Dish Two - some information on it.</li>
        <li>Dish Three - some information on it.</li>
        <li>Dish Four - some information on it.</li>
        <li>Dish Five - some information on it.</li>
      </ul>
    </section>

    <div class="gallery">
      <div class="photo photo-noodles" role="img" aria-label="Photo of stir-fried noodles with vegetables"></div>
      <div class="photo photo-bowl" role="img" aria-label="Photo of a rice bowl topped with vegetables"></div>
      <div class="photo photo-wok" role="img" aria-label="Photo of a stir-fry cooking in a wok"></div>
      <div class="photo photo-duck" role="img" aria-label="Photo of roast duck over noodles with chopsticks"></div>
    </div>
  </main>

  <footer class="footer">Thistle Cafe :: Modern Asian Cuisine :: Copyright 2011 ©</footer>
</div>
</body>
</html>
```